Talvix Inc

Hello.

I would like to take a wordpress ecomm template and turn it into a website that can display 100s of domain listings with short text box for description and a price .
One link to quorvend.example for immediate payment and with the confirmation/decline letter/email .
Five - six pages, Home, about us, domains, contact us, . Several columns or scrolling page for the domain page. I want to list several hundred virtual domains for sale .
Like a portfolio website but lists domain text .
This will be hosted on my server. On my domain.

Target Market(s)

End users, business owners, store front managers, online entpenauers , ect

Industry/Entity Type

Information Technology

Number of Pages Required

5+ page

Font styles to use
Sans Serif

Colors
0455a3
f78f20
abd036

Requirements
Must have
• Lots of white space, clean professional look . fast loading , use of greens and blues. Easy to read font.
• big headers , several - three different headers that rotate or move or clicks.
• A few current stock photos.
Should not have
• slow loading photos.
• More than two photos on any one page.

```html
<!DOCTYPE html>
<html lang="en">
<head>
<meta charset="utf-8">
<title>Talvix Domains</title>
<link href="https://fonts.googleapis.com/css2?family=Lato:ital,wght@0,400;0,700;0,900;1,400&family=Ubuntu:wght@400;500;700&display=swap" rel="stylesheet">
<style>
:root{
  --green:#abd036;
  --blue:#0455a3;
  --orange:#f78f20;
  --dark:#23262e;
  --ink:#111;
  --grey-bg:#f3f3f3;
  --card-bg:#fafafa;
  --line:#e2e2e2;
  --white:#fff;
}
*{box-sizing:border-box;margin:0;padding:0}
html,body{width:1200px;height:2359px;overflow:hidden}
body{font-family:"Lato",sans-serif;color:var(--ink);background:var(--white);position:relative}
a{color:inherit;text-decoration:none}

.topbar{position:absolute;top:0;left:0;width:1200px;height:35px;background:var(--green);color:var(--white);font-size:13px;font-weight:700}
.topbar .contact{position:absolute;left:88px;top:0;height:35px;display:flex;align-items:center;gap:22px}
.topbar .contact span{display:flex;align-items:center;gap:7px}
.topbar .account{position:absolute;right:88px;top:0;height:35px;display:flex;align-items:center}
.topbar .account span{display:flex;align-items:center;gap:7px;padding:0 14px}
.topbar .account span+span{border-left:1px solid rgba(255,255,255,.5)}
.topbar .account span:last-child{padding-right:0}

.header{position:absolute;top:35px;left:0;width:1200px;height:70px}
.brand{position:absolute;left:88px;top:12px;font-family:"Ubuntu",sans-serif;font-weight:500;font-size:41px;color:var(--ink);letter-spacing:-.3px}
.nav{position:absolute;right:86px;top:0;height:70px;display:flex;align-items:center;gap:40px;font-family:"Ubuntu",sans-serif;font-weight:500;font-size:17px}
.nav .active{color:var(--green)}

.hero{position:absolute;top:105px;left:0;width:1200px;height:412px;background:linear-gradient(90deg,#b9b9b7 0%,#cfcecb 35%,#e6e1da 60%,#bfae98 100%)}
.hero-photo{position:absolute;right:0;top:0;width:680px;height:412px;background:linear-gradient(100deg,rgba(255,255,255,0) 0%,#efe8df 25%,#d9c6ad 60%,#8a7863 100%)}
.hero-base{position:absolute;left:0;bottom:0;width:540px;height:55px;background:linear-gradient(180deg,#2a3f66 0,#1a1c22 6px,#15171c 100%)}
.search{position:absolute;left:88px;top:118px;display:flex;gap:11px}
.search .field{width:370px;height:38px;background:#5b5b5b;border-radius:3px;color:#ddd;font-size:12px;font-style:italic;display:flex;align-items:center;padding-left:16px;position:relative}
.search .field .tld{position:absolute;right:20px;font-style:normal;color:#aaa;padding-left:12px;border-left:1px solid #888}
.search .btn{width:133px;height:38px;background:var(--orange);color:var(--white);border-radius:3px;font-size:14px;font-weight:700;display:flex;align-items:center;justify-content:center}
.tlds{position:absolute;left:88px;top:188px;display:flex;gap:44px;font-size:12px}
.tlds span{display:flex;align-items:center;gap:16px}
.tlds i{width:12px;height:12px;background:var(--white);border:1px solid #999;display:block}
.services{position:absolute;left:88px;top:245px;display:flex;gap:0;font-size:12px;font-weight:700;color:var(--dark)}
.services div{display:flex;flex-direction:column;align-items:center;gap:6px;width:124px}
.services div+div{margin-left:40px}

.welcome{position:absolute;top:517px;left:0;width:1200px;height:291px;background:var(--grey-bg);text-align:center}
.welcome h1{font-family:"Ubuntu",sans-serif;font-weight:500;font-size:37px;margin-top:38px;letter-spacing:-.2px}
.welcome p{width:1010px;margin:18px auto 0;font-size:14.5px;line-height:22px;color:#222}

.pill{position:absolute;height:35px;display:flex;align-items:center;background:var(--blue);color:var(--white);font-size:14px;font-weight:700;border-radius:3px;overflow:hidden}
.pill .label{padding-left:10px;flex:1}
.pill svg{display:block}

.section-title{position:absolute;top:838px;left:0;width:1200px;text-align:center;font-family:"Ubuntu",sans-serif;font-weight:500;font-size:34px}

.card{position:absolute;width:214px;height:236px;background:var(--card-bg);border:1px solid var(--line);text-align:center}
.card svg.top{position:absolute;left:-1px;top:-1px}
.card .domain{position:absolute;top:14px;left:0;width:100%;color:var(--white);font-size:12.5px}
.card .price{position:absolute;left:64px;top:48px;width:84px;height:84px;border-radius:50%;background:var(--white);box-shadow:0 2px 5px rgba(0,0,0,.25);border:2px solid #ececec;display:flex;align-items:center;justify-content:center;font-weight:700;font-size:22px;color:var(--ink)}
.card .price sup{font-size:10px;margin-right:1px;vertical-align:10px}
.card .price small{font-size:10px;vertical-align:-4px}
.card .desc{position:absolute;top:141px;left:0;width:100%;font-size:11.5px;line-height:16px;color:#222}
.card .buy{position:absolute;top:185px;left:55px;width:104px;height:29px;background:var(--green);color:var(--white);font-size:12.5px;font-weight:700;border-radius:2px;display:flex;align-items:center;justify-content:center;gap:9px}

.banner{position:absolute;top:2117px;left:88px;width:1022px;height:93px}
.banner .left{position:absolute;left:0;top:0;width:368px;height:93px;background:linear-gradient(90deg,#1a1e26,#253343);display:flex;align-items:center;padding-left:17px;font-family:"Ubuntu",sans-serif;font-weight:500;font-size:33px;color:var(--white)}
.banner .right{position:absolute;left:372px;top:0;width:650px;height:93px;background:linear-gradient(90deg,#2a4258 0%,#3a6e96 45%,#2d8fcf 100%);overflow:hidden}
.banner .right h2{position:absolute;left:0;width:520px;top:12px;text-align:center;font-family:"Ubuntu",sans-serif;font-weight:500;font-size:29px;color:var(--white)}
.banner .right h2 em{font-style:normal;color:var(--orange)}
.banner .right p{position:absolute;left:0;width:520px;top:52px;text-align:center;font-size:14px;color:var(--white)}
.banner .ribbon{position:absolute;right:0;bottom:0}

.footer{position:absolute;top:2252px;left:0;width:1200px;height:107px;background:var(--blue);color:var(--white)}
.footer .help{position:absolute;top:13px;left:0;width:100%;text-align:center;font-size:20px;font-weight:700}
.footer .rule{position:absolute;top:53px;left:88px;width:1022px;height:1px;background:rgba(255,255,255,.2)}
.footer .links{position:absolute;left:88px;top:68px;display:flex;gap:20px;font-size:13.5px}
.footer .copy{position:absolute;right:88px;top:68px;font-size:13.5px}
</style>
</head>
<body>

<div class="topbar">
  <div class="contact">
    <span><svg width="14" height="14" viewBox="0 0 24 24"><path fill="#fff" d="M6.6 10.8a15.1 15.1 0 0 0 6.6 6.6l2.2-2.2a1 1 0 0 1 1-.25 11.4 11.4 0 0 0 3.6.57 1 1 0 0 1 1 1V20a1 1 0 0 1-1 1A17 17 0 0 1 3 4a1 1 0 0 1 1-1h3.5a1 1 0 0 1 1 1c0 1.250.2 2.45.57 3.57a1 1 0 0 1-.25 1z"/></svg>555.010.4477</span>
    <span><svg width="14" height="11" viewBox="0 0 14 11"><rect width="14" height="11" fill="#fff"/><path d="M0 0l7 6 7-6" fill="none" stroke="#abd036" stroke-width="1.4"/></svg>info@talvixdomains.example</span>
  </div>
  <div class="account">
    <span><svg width="14" height="14" viewBox="0 0 14 14"><circle cx="7" cy="4" r="3.3" fill="#fff"/><path d="M0 14c0-4 3-6 7-6s7 2 7 6z" fill="#fff"/></svg>Login</span>
    <span><svg width="16" height="14" viewBox="0 0 16 14"><circle cx="6" cy="4" r="3.3" fill="#fff"/><path d="M0 14c0-4 2.5-6 6-6s6 2 6 6z" fill="#fff"/><path d="M13 3v6M10 6h6" stroke="#fff" stroke-width="1.6"/></svg>Sign In</span>
  </div>
</div>

<header class="header">
  <div class="brand">Talvix Domains</div>
  <nav class="nav">
    <a class="active">Home</a><a>About Us</a><a>Domains</a><a>Contacts</a>
  </nav>
</header>

<section class="hero">
  <div class="hero-photo" role="img" aria-label="Stock photo of three smiling colleagues working together at a laptop in a bright office"></div>
  <div class="hero-base"></div>
  <div class="search">
    <div class="field">Enter your domain...<span class="tld">.com</span></div>
    <div class="btn">Search Domain</div>
  </div>
  <div class="tlds">
    <span><i></i>.com</span><span><i></i>.biz</span><span><i></i>.ws</span><span><i></i>.co</span><span><i></i>.org</span>
  </div>
  <div class="services">
    <div>
      <svg width="28" height="28" viewBox="0 0 28 28"><circle cx="14" cy="14" r="12" fill="none" stroke="#0455a3" stroke-width="2"/><ellipse cx="14" cy="14" rx="5" ry="12" fill="none" stroke="#0455a3" stroke-width="1.5"/><rect x="2" y="10.5" width="24" height="7" fill="#0455a3"/><text x="14" y="16.3" text-anchor="middle" font-size="5.5" font-family="Lato,sans-serif" font-weight="700" fill="#fff">www</text></svg>
      REGISTER DOMAINS
    </div>
    <div>
      <svg width="32" height="28" viewBox="0 0 32 28"><path d="M8 22a6 6 0 0 1 0-12 8 8 0 0 1 15-2 7 7 0 0 1 1 14z" fill="none" stroke="#0455a3" stroke-width="2"/><path d="M12 16a4 4 0 0 1 7-2m1 2a4 4 0 0 1-7 2" fill="none" stroke="#0455a3" stroke-width="1.6"/><path d="M19 11v3h-3M13 21v-3h3" fill="none" stroke="#0455a3" stroke-width="1.4"/></svg>
      TRANSFER DOMAINS
    </div>
    <div>
      <svg width="32" height="28" viewBox="0 0 32 28"><path d="M8 22a6 6 0 0 1 0-12 8 8 0 0 1 15-2 7 7 0 0 1 1 14z" fill="none" stroke="#0455a3" stroke-width="2"/><circle cx="13" cy="15" r="2.5" fill="none" stroke="#0455a3" stroke-width="1.5"/><circle cx="19.5" cy="15" r="2.5" fill="none" stroke="#0455a3" stroke-width="1.5"/></svg>
      MANAGE DOMAINS
    </div>
  </div>
</section>

<section class="welcome">
  <h1>Welcome To Talvix Domains</h1>
  <p>Lorem ipsum dolor sit amet, consectetuer adipiscing elit, sed diam nonummy nibh euismod tincidunt ut laoreet dolore magna aliquam erat volutpat. Ut wisi enim ad minim veniam, quis nostrud exerci tation ullamcorper suscipit lobortis nisl ut aliquip ex ea commodo consequat. Duis autem vel eum iriure dolor in hendrerit in vulputate velit esse molestie consequat, vel illum dolore eu feugiat nulla facilisis at vero eros et accumsan et iusto odio dignissim qui blandit praesent luptatum zzril delenit augue duis dolore te feugait nulla facilisi.</p>
</section>
<a class="pill" style="left:543px;top:738px;width:114px">
  <span class="label">Read More</span>
  <svg width="30" height="35" viewBox="0 0 30 35"><polygon points="8,0 30,0 30,35 0,35" fill="#f78f20"/><path d="M15 13l4 4.5-4 4.5" fill="none" stroke="#fff" stroke-width="1.8"/></svg>
</a>

<h2 class="section-title">LIST OF DOMAINS FOR SALE</h2>

<div class="card" style="left:88px;top:936px"><svg class="top" width="214" height="116"><polygon points="0,0 214,0 214,82 107,115 0,82" fill="#23262e"/></svg><div class="domain">www.lorenipsum .example</div><div class="price"><sup>$</sup>17<small>.00</small></div><div class="desc">Lorem ipsum dolor sit amet, sect<br>adipiscing elit, sed diam</div><div class="buy"><svg width="16" height="14" viewBox="0 0 16 14"><path d="M0 1h3l2 8h9l2-6H4" fill="none" stroke="#0455a3" stroke-width="1.6"/><circle cx="6" cy="12" r="1.4" fill="#0455a3"/><circle cx="13" cy="12" r="1.4" fill="#0455a3"/></svg>Buy Now</div></div>
<div class="card" style="left:359px;top:936px"><svg class="top" width="214" height="116"><polygon points="0,0 214,0 214,82 107,115 0,82" fill="#23262e"/></svg><div class="domain">www.lorenipsum .example</div><div class="price"><sup>$</sup>12<small>.00</small></div><div class="desc">Lorem ipsum dolor sit amet, sect<br>adipiscing elit, sed diam</div><div class="buy"><svg width="16" height="14" viewBox="0 0 16 14"><path d="M0 1h3l2 8h9l2-6H4" fill="none" stroke="#0455a3" stroke-width="1.6"/><circle cx="6" cy="12" r="1.4" fill="#0455a3"/><circle cx="13" cy="12" r="1.4" fill="#0455a3"/></svg>Buy Now</div></div>
<div class="card" style="left:629px;top:919px"><svg class="top" width="214" height="116"><polygon points="0,0 214,0 214,82 107,115 0,82" fill="#f78f20"/></svg><div class="domain">www.lorenipsum .example</div><div class="price"><sup>$</sup>21<small>.00</small></div><div class="desc">Lorem ipsum dolor sit amet, sect<br>adipiscing elit, sed diam</div><div class="buy"><svg width="16" height="14" viewBox="0 0 16 14"><path d="M0 1h3l2 8h9l2-6H4" fill="none" stroke="#0455a3" stroke-width="1.6"/><circle cx="6" cy="12" r="1.4" fill="#0455a3"/><circle cx="13" cy="12" r="1.4" fill="#0455a3"/></svg>Buy Now</div></div>
<div class="card" style="left:900px;top:936px"><svg class="top" width="214" height="116"><polygon points="0,0 214,0 214,82 107,115 0,82" fill="#23262e"/></svg><div class="domain">www.lorenipsum .example</div><div class="price"><sup>$</sup>09<small>.00</small></div><div class="desc">Lorem ipsum dolor sit amet, sect<br>adipiscing elit, sed diam</div><div class="buy"><svg width="16" height="14" viewBox="0 0 16 14"><path d="M0 1h3l2 8h9l2-6H4" fill="none" stroke="#0455a3" stroke-width="1.6"/><circle cx="6" cy="12" r="1.4" fill="#0455a3"/><circle cx="13" cy="12" r="1.4" fill="#0455a3"/></svg>Buy Now</div></div>

<div class="card" style="left:88px;top:1208px"><svg class="top" width="214" height="116"><polygon points="0,0 214,0 214,82 107,115 0,82" fill="#23262e"/></svg><div class="domain">www.lorenipsum .example</div><div class="price"><sup>$</sup>17<small>.00</small></div><div class="desc">Lorem ipsum dolor sit amet, sect<br>adipiscing elit, sed diam</div><div class="buy"><svg width="16" height="14" viewBox="0 0 16 14"><path d="M0 1h3l2 8h9l2-6H4" fill="none" stroke="#0455a3" stroke-width="1.6"/><circle cx="6" cy="12" r="1.4" fill="#0455a3"/><circle cx="13" cy="12" r="1.4" fill="#0455a3"/></svg>Buy Now</div></div>
<div class="card" style="left:359px;top:1208px"><svg class="top" width="214" height="116"><polygon points="0,0 214,0 214,82 107,115 0,82" fill="#23262e"/></svg><div class="domain">www.lorenipsum .example</div><div class="price"><sup>$</sup>16<small>.00</small></div><div class="desc">Lorem ipsum dolor sit amet, sect<br>adipiscing elit, sed diam</div><div class="buy"><svg width="16" height="14" viewBox="0 0 16 14"><path d="M0 1h3l2 8h9l2-6H4" fill="none" stroke="#0455a3" stroke-width="1.6"/><circle cx="6" cy="12" r="1.4" fill="#0455a3"/><circle cx="13" cy="12" r="1.4" fill="#0455a3"/></svg>Buy Now</div></div>
<div class="card" style="left:629px;top:1208px"><svg class="top" width="214" height="116"><polygon points="0,0 214,0 214,82 107,115 0,82" fill="#23262e"/></svg><div class="domain">www.lorenipsum .example</div><div class="price"><sup>$</sup>11<small>.00</small></div><div class="desc">Lorem ipsum dolor sit amet, sect<br>adipiscing elit, sed diam</div><div class="buy"><svg width="16" height="14" viewBox="0 0 16 14"><path d="M0 1h3l2 8h9l2-6H4" fill="none" stroke="#0455a3" stroke-width="1.6"/><circle cx="6" cy="12" r="1.4" fill="#0455a3"/><circle cx="13" cy="12" r="1.4" fill="#0455a3"/></svg>Buy Now</div></div>
<div class="card" style="left:900px;top:1208px"><svg class="top" width="214" height="116"><polygon points="0,0 214,0 214,82 107,115 0,82" fill="#23262e"/></svg><div class="domain">www.lorenipsum .example</div><div class="price"><sup>$</sup>09<small>.00</small></div><div class="desc">Lorem ipsum dolor sit amet, sect<br>adipiscing elit, sed diam</div><div class="buy"><svg width="16" height="14" viewBox="0 0 16 14"><path d="M0 1h3l2 8h9l2-6H4" fill="none" stroke="#0455a3" stroke-width="1.6"/><circle cx="6" cy="12" r="1.4" fill="#0455a3"/><circle cx="13" cy="12" r="1.4" fill="#0455a3"/></svg>Buy Now</div></div>

<div class="card" style="left:88px;top:1479px"><svg class="top" width="214" height="116"><polygon points="0,0 214,0 214,82 107,115 0,82" fill="#23262e"/></svg><div class="domain">www.lorenipsum .example</div><div class="price"><sup>$</sup>19<small>.00</small></div><div class="desc">Lorem ipsum dolor sit amet, sect<br>adipiscing elit, sed diam</div><div class="buy"><svg width="16" height="14" viewBox="0 0 16 14"><path d="M0 1h3l2 8h9l2-6H4" fill="none" stroke="#0455a3" stroke-width="1.6"/><circle cx="6" cy="12" r="1.4" fill="#0455a3"/><circle cx="13" cy="12" r="1.4" fill="#0455a3"/></svg>Buy Now</div></div>
<div class="card" style="left:359px;top:1479px"><svg class="top" width="214" height="116"><polygon points="0,0 214,0 214,82 107,115 0,82" fill="#23262e"/></svg><div class="domain">www.lorenipsum .example</div><div class="price"><sup>$</sup>17<small>.00</small></div><div class="desc">Lorem ipsum dolor sit amet, sect<br>adipiscing elit, sed diam</div><div class="buy"><svg width="16" height="14" viewBox="0 0 16 14"><path d="M0 1h3l2 8h9l2-6H4" fill="none" stroke="#0455a3" stroke-width="1.6"/><circle cx="6" cy="12" r="1.4" fill="#0455a3"/><circle cx="13" cy="12" r="1.4" fill="#0455a3"/></svg>Buy Now</div></div>
<div class="card" style="left:629px;top:1479px"><svg class="top" width="214" height="116"><polygon points="0,0 214,0 214,82 107,115 0,82" fill="#23262e"/></svg><div class="domain">www.lorenipsum .example</div><div class="price"><sup>$</sup>12<small>.00</small></div><div class="desc">Lorem ipsum dolor sit amet, sect<br>adipiscing elit, sed diam</div><div class="buy"><svg width="16" height="14" viewBox="0 0 16 14"><path d="M0 1h3l2 8h9l2-6H4" fill="none" stroke="#0455a3" stroke-width="1.6"/><circle cx="6" cy="12" r="1.4" fill="#0455a3"/><circle cx="13" cy="12" r="1.4" fill="#0455a3"/></svg>Buy Now</div></div>
<div class="card" style="left:900px;top:1479px"><svg class="top" width="214" height="116"><polygon points="0,0 214,0 214,82 107,115 0,82" fill="#23262e"/></svg><div class="domain">www.lorenipsum .example</div><div class="price"><sup>$</sup>23<small>.00</small></div><div class="desc">Lorem ipsum dolor sit amet, sect<br>adipiscing elit, sed diam</div><div class="buy"><svg width="16" height="14" viewBox="0 0 16 14"><path d="M0 1h3l2 8h9l2-6H4" fill="none" stroke="#0455a3" stroke-width="1.6"/><circle cx="6" cy="12" r="1.4" fill="#0455a3"/><circle cx="13" cy="12" r="1.4" fill="#0455a3"/></svg>Buy Now</div></div>

<div class="card" style="left:88px;top:1750px"><svg class="top" width="214" height="116"><polygon points="0,0 214,0 214,82 107,115 0,82" fill="#23262e"/></svg><div class="domain">www.lorenipsum .example</div><div class="price"><sup>$</sup>09<small>.00</small></div><div class="desc">Lorem ipsum dolor sit amet, sect<br>adipiscing elit, sed diam</div><div class="buy"><svg width="16" height="14" viewBox="0 0 16 14"><path d="M0 1h3l2 8h9l2-6H4" fill="none" stroke="#0455a3" stroke-width="1.6"/><circle cx="6" cy="12" r="1.4" fill="#0455a3"/><circle cx="13" cy="12" r="1.4" fill="#0455a3"/></svg>Buy Now</div></div>
<div class="card" style="left:359px;top:1750px"><svg class="top" width="214" height="116"><polygon points="0,0 214,0 214,82 107,115 0,82" fill="#23262e"/></svg><div class="domain">www.lorenipsum .example</div><div class="price"><sup>$</sup>13<small>.00</small></div><div class="desc">Lorem ipsum dolor sit amet, sect<br>adipiscing elit, sed diam</div><div class="buy"><svg width="16" height="14" viewBox="0 0 16 14"><path d="M0 1h3l2 8h9l2-6H4" fill="none" stroke="#0455a3" stroke-width="1.6"/><circle cx="6" cy="12" r="1.4" fill="#0455a3"/><circle cx="13" cy="12" r="1.4" fill="#0455a3"/></svg>Buy Now</div></div>
<div class="card" style="left:629px;top:1750px"><svg class="top" width="214" height="116"><polygon points="0,0 214,0 214,82 107,115 0,82" fill="#23262e"/></svg><div class="domain">www.lorenipsum .example</div><div class="price"><sup>$</sup>15<small>.00</small></div><div class="desc">Lorem ipsum dolor sit amet, sect<br>adipiscing elit, sed diam</div><div class="buy"><svg width="16" height="14" viewBox="0 0 16 14"><path d="M0 1h3l2 8h9l2-6H4" fill="none" stroke="#0455a3" stroke-width="1.6"/><circle cx="6" cy="12" r="1.4" fill="#0455a3"/><circle cx="13" cy="12" r="1.4" fill="#0455a3"/></svg>Buy Now</div></div>
<div class="card" style="left:900px;top:1750px"><svg class="top" width="214" height="116"><polygon points="0,0 214,0 214,82 107,115 0,82" fill="#23262e"/></svg><div class="domain">www.lorenipsum .example</div><div class="price"><sup>$</sup>21<small>.00</small></div><div class="desc">Lorem ipsum dolor sit amet, sect<br>adipiscing elit, sed diam</div><div class="buy"><svg width="16" height="14" viewBox="0 0 16 14"><path d="M0 1h3l2 8h9l2-6H4" fill="none" stroke="#0455a3" stroke-width="1.6"/><circle cx="6" cy="12" r="1.4" fill="#0455a3"/><circle cx="13" cy="12" r="1.4" fill="#0455a3"/></svg>Buy Now</div></div>

<a class="pill" style="left:543px;top:2024px;width:114px">
  <span class="label" style="padding-left:18px">View All</span>
  <svg width="30" height="35" viewBox="0 0 30 35"><polygon points="8,0 30,0 30,35 0,35" fill="#f78f20"/><path d="M15 13l4 4.5-4 4.5" fill="none" stroke="#fff" stroke-width="1.8"/></svg>
</a>

<aside class="banner">
  <div class="left">Talvix Domains</div>
  <div class="right" role="img" aria-label="Blue backdrop with a faint world map promoting the domain community">
    <h2>The <em>Largest</em> Domain Community</h2>
    <p>Learn. Share. Profit. All For Free!</p>
    <svg class="ribbon" width="70" height="55" viewBox="0 0 70 55"><polygon points="70,0 70,28 28,55 0,55" fill="#f78f20"/><text x="50" y="44" transform="rotate(-33 50 44)" text-anchor="middle" font-family="Lato,sans-serif" font-style="italic" font-weight="700" font-size="14" fill="#fff">Free</text></svg>
  </div>
</aside>

<footer class="footer">
  <div class="help">Need Help?&nbsp; Call Our Award-winning Support Team 24/7 At 555-010-4477</div>
  <div class="rule"></div>
  <nav class="links"><a>Home</a><a>About Us</a><a>Domains</a><a>Contacts</a></nav>
  <div class="copy">Copyright © 2016 Talvix Domains. All Rights Reserved.</div>
</footer>

</body>
</html>
```